Programme Management Specialists based in London focused on providing a PMO service to run Business

We need a new wordpress design template that will allow us to populate the content using wordpress

1) We have logo and colour theme ( I will upload)

1) I needs it to be mobile optimised.

Proposition
We are an independent and technology agnostic programme office (PMO) providing highly specialised managed service capable of setting up & delivering large scale business transformation programmes as a result of digitalisation.

By setting up a temporary environment within your environment , we provide the required structure, processes and expertise to deliver company wide organisational & operational change as a consequence of digital innovation.

WE ARE NOT AN IT FIRM - BUT PROJECT MANAGEMENT FIRM. WE MANAGE ALL ELEMENTS OF THE PROJECT (IT, ECOMMECE, LOGISTICS, FINANCE, HR, SUPPLY CHAIN, CALL CENTRE, SHOPS) to ensure the right OUTCOME.

A LITTLE EXTRA:
We provide structure during change giving the confidence required during a period of uncertainty

INDUSTRY
RETAIL & MEDIA

Hi, I thought it may help if I mentioned a few other things I see us like a conductor of an orchestra - without is you have a bunch of talented musicians but no symphony. Also more depth about what we do: A little more background - The site Pages Wordpress website(non transactional) Build mobile first Blog section Proposition We are an independent and technology agnostic programme office (PMO) providing highly specialised managed service capable of setting up & delivering large scale business transformation programmes as a result of digitalisation. By setting up a temporary environment within your environment , we provide the required structure, processes and expertise to agressively deliver conpany wide organisational & operational change as a consequence of digital innovation. Extra 1)We provide structure during change giving the confidence required during a period of uncertainty 2) we are project management (not IT) Our signature KVN : Transforming your vision into reality Our Services 1. programme Management 2. Digital Transformation delivery consultancy 4. full PMO service(programme management, risk management, change management, communication strategy) 5. Audit exiting programmes - 6. RECOVERY - ensure programmes than have gone awry are put back on track. 7. Business process re-engineering Change often comes through execution, the key to our service is that throughout our engagement we work closely with your staff to embed a culture of perpetual change capable of delivering at pace your customers expects long after we leave. The Industries we target Retail Media Travel So why is this important to our clients: Our approach leads to efficiency and helps deliver projects even better, faster and cheaper. We educate organisations to understand that project management processes should be implemented consistently across the organization thus allowing true business transformation. Many companies give this responsibility to one or more people in a Project Management Office (PMO). There are many structures for a PMO and many types of services that we can offer. We help organization to firstly determine the services that are important to them and then create an overall approach to implementing. Since this is a culture change initiative, the effort can be time-consuming and difficult. However, the rewards are also large. We ensure the PMO is established with a clear vision, strong sponsorship and a solid approach, creating a vehicle for providing a tremendous amount of value for the company.

```html
<!DOCTYPE html>
<html lang="en">
<head>
<meta charset="utf-8">
<title>KVN Programme Partners — Blog</title>
<link href="https://fonts.googleapis.com/css2?family=Arimo:wght@400;700&family=Pathway+Gothic+One&display=swap" rel="stylesheet">
<style>
  :root{
    --gold:#eea800;
    --ink:#333333;
    --panel:#eeeeee;
    --footer:#3d3d3d;
    --white:#ffffff;
    --photo-a:#a0703c;
    --photo-b:#5c3a22;
  }
  *{box-sizing:border-box;margin:0;padding:0}
  html,body{width:1200px;height:1143px;overflow:hidden;background:var(--white)}
  body{font-family:"Arimo",Arial,sans-serif;color:var(--ink);position:relative}
  .abs{position:absolute}
  ul{list-style:none}

  /* header */
  .brand{left:79px;top:30px;display:flex;align-items:center;gap:14px}
  .brand-mark{width:46px;height:46px;background:var(--gold)}
  .brand-text{border-left:1px solid #ccc;padding-left:12px}
  .brand-name{font-size:22px;font-weight:700;color:var(--ink);line-height:1.2}
  .brand-tag{font-size:8px;font-weight:700;color:var(--ink);margin-top:6px;letter-spacing:.2px}
  .main-nav a{position:absolute;top:52px;font-size:14px;font-weight:700;color:var(--ink);text-decoration:none}
  .main-nav .blog{top:41px;left:1008px;width:88px;height:41px;border:1px solid var(--gold);display:flex;align-items:center;justify-content:center}
  .header-rule{left:0;top:133px;width:1200px;height:5px;background:var(--gold)}

  /* posts */
  .post{left:77px;width:688px;height:334px;background:var(--panel);border-top:4px solid var(--gold)}
  .post-title{position:absolute;left:25px;top:22px;font-family:"Pathway Gothic One",sans-serif;font-size:30px;color:var(--gold);text-transform:uppercase;letter-spacing:-.2px}
  .post-photo{position:absolute;left:28px;top:71px;width:209px;height:138px;background:linear-gradient(135deg,var(--photo-a),var(--photo-b))}
  .post-lead{position:absolute;left:253px;top:67px;width:389px;font-size:13px;line-height:23px;letter-spacing:.9px;text-align:justify;text-align-last:justify}
  .post-excerpt{position:absolute;left:25px;top:226px;width:620px;font-size:13px;line-height:23px;letter-spacing:.2px}
  .read-more{position:absolute;right:50px;top:279px;font-size:14px;font-weight:700;color:var(--gold);text-decoration:none}
  .post-meta{position:absolute;left:25px;top:302px;font-size:12px;color:#111}

  /* sidebar */
  .widget{left:796px;width:313px;background:var(--panel);border-top:4px solid var(--gold)}
  .widget-title{font-family:"Pathway Gothic One",sans-serif;font-size:28px;color:var(--gold);text-transform:uppercase;text-align:center;margin-top:20px}
  .widget ul{position:absolute;left:20px;top:64px}
  .widget li{position:relative;padding-left:21px;font-size:14px;font-weight:700;height:31.3px}
  .widget li::before{content:"";position:absolute;left:0;top:4px;width:5px;height:5px;background:var(--ink)}
  .widget li.active{color:var(--gold)}
  .widget li.active::before{background:var(--gold)}
  .recent li{height:52px;color:var(--gold)}
  .recent li::before{background:var(--gold)}
  .recent time{display:block;font-weight:400;font-size:13px;color:var(--ink);margin-top:6px}

  /* footer */
  .site-footer{left:0;top:892px;width:1200px;height:251px;background:var(--footer)}
  .foot-nav{left:107px;top:14px}
  .foot-nav li{font-size:14px;font-weight:700;color:var(--white);height:31.3px}
  .foot-nav li.active{color:var(--gold)}
  .foot-contact{left:441px;top:45px}
  .foot-contact li{font-size:14px;font-weight:700;color:var(--white);height:31.3px}
  .follow{left:796px;top:16px;font-family:"Pathway Gothic One",sans-serif;font-size:26px;color:var(--gold)}
  .social{left:796px;top:60px}
  .foot-rule{left:0;top:208px;width:1200px;height:1px;background:#5a5a5a}
  .copyright{left:0;top:221px;width:1200px;text-align:center;font-size:12px;color:var(--gold)}
  .copyright b{color:var(--white)}
</style>
</head>
<body>

<header>
  <div class="abs brand">
    <span class="brand-mark"></span>
    <div class="brand-text">
      <div class="brand-name">KVN Programme Partners</div>
      <div class="brand-tag">TRANSFORMING YOUR VISION INTO REALITY</div>
    </div>
  </div>
  <nav class="main-nav">
    <a href="#" style="left:575px">HOME</a>
    <a href="#" style="left:669px">ABOUT</a>
    <a href="#" style="left:769px">CAPABILITIES</a>
    <a href="#" style="left:912px">CONTACT</a>
    <a href="#" class="blog">BLOG</a>
  </nav>
  <div class="abs header-rule"></div>
</header>

<main>
  <article class="abs post" style="top:159px">
    <h2 class="post-title">Lorem Ipsum is simply dummy text of the printing</h2>
    <div class="post-photo" role="img" aria-label="Photo of a workshop session in a meeting room"></div>
    <p class="post-lead">Lorem Ipsum is simply dummy text of the printing and typesetting industry. Lorem Ipsum has been the industry's standard dummy text ever since the 1500s, when an unknown printer took a galley of type and scrambled it to make a type specimen book. It has one lore ipsum is simply dummy text Lorem Ipsum is simply dummy text of the printing.</p>
    <p class="post-excerpt">Lorem Ipsum is simply dummy text of the printing and typesetting industry. Lorem Ipsum has been the industry's standard dummy text ever since the 1500s, when an unknown printer took a galley...</p>
    <a href="#" class="read-more">CONTINUE READING</a>
    <p class="post-meta">News , 25 SEptember 2014</p>
  </article>

  <article class="abs post" style="top:515px">
    <h2 class="post-title">Lorem Ipsum is simply dummy text of the printing</h2>
    <div class="post-photo" role="img" aria-label="Photo of a workshop session in a meeting room"></div>
    <p class="post-lead">Lorem Ipsum is simply dummy text of the printing and typesetting industry. Lorem Ipsum has been the industry's standard dummy text ever since the 1500s, when an unknown printer took a galley of type and scrambled it to make a type specimen book. It has one lore ipsum is simply dummy text Lorem Ipsum is simply dummy text of the printing.</p>
    <p class="post-excerpt">Lorem Ipsum is simply dummy text of the printing and typesetting industry. Lorem Ipsum has been the industry's standard dummy text ever since the 1500s, when an unknown printer took a galley...</p>
    <a href="#" class="read-more">CONTINUE READING</a>
    <p class="post-meta">News , 25 SEptember 2014</p>
  </article>
</main>

<aside>
  <section class="abs widget" style="top:159px;height:198px">
    <h3 class="widget-title">Categories</h3>
    <ul>
      <li class="active">NEWS</li>
      <li>EVENTS</li>
      <li>ARTICLES</li>
      <li>PRESS</li>
    </ul>
  </section>
  <section class="abs widget recent" style="top:378px;height:229px">
    <h3 class="widget-title">Recent Posts</h3>
    <ul>
      <li>Lorem Ipsum is simply<time>25 September 2014</time></li>
      <li>Lorem Ipsum is simply<time>25 September 2014</time></li>
      <li>Lorem Ipsum is simply<time>25 September 2014</time></li>
    </ul>
  </section>
  <section class="abs widget" style="top:628px;height:219px">
    <h3 class="widget-title" style="text-align:left;padding-left:82px">Archives</h3>
    <ul>
      <li class="active">2014</li>
      <li>2013</li>
      <li>2012</li>
      <li>2011</li>
    </ul>
  </section>
</aside>

<footer class="abs site-footer">
  <ul class="abs foot-nav">
    <li class="active">HOME</li>
    <li>ABOUT</li>
    <li>EXPERTISE</li>
    <li>SULOTIONS</li>
    <li>INDUSTRIES</li>
    <li>CONTACT</li>
  </ul>
  <ul class="abs foot-contact">
    <li>Office No., Building Name,</li>
    <li>Area, Near Area,</li>
    <li>City, State, Country</li>
    <li>Call : +44 100 200 3000</li>
    <li>Email : info@kvnprogramme.example</li>
  </ul>
  <div class="abs follow">FOLLOW US ON :</div>
  <svg class="abs social" width="300" height="125" viewBox="0 0 300 125" aria-label="Social links">
    <g fill="none" stroke="#eea800" stroke-width="1.5">
      <circle cx="23" cy="23" r="22.5" fill="#eea800"/>
      <circle cx="104" cy="23" r="22.5"/>
      <circle cx="186" cy="23" r="22.5"/>
      <circle cx="265" cy="23" r="22.5"/>
      <circle cx="23" cy="97" r="22.5"/>
      <circle cx="104" cy="97" r="22.5"/>
      <circle cx="186" cy="97" r="22.5"/>
      <circle cx="267" cy="97" r="22.5"/>
    </g>
  </svg>
  <div class="abs foot-rule"></div>
  <p class="abs copyright">© <b>KVNProgrammePartners</b> - 2014. All Rights Reserved. <b>Privacy Policy.</b></p>
</footer>

</body>
</html>
```